Your Health, Your Time, Your Way: Personalized, Concierge Care Elevated to Modern Medicine

We need to incorporate an image of our new doctor (Dr. Malvina Okoruwe, MD) with our office logo ( Harborline Family Clinic) and dialogue that shows how simple it is to schedule a free consult and learn what our office has to offer patients. The colors should be consistent with our website- the CMYK codes will be attached for your use below. The font should be easy to read. The text should be clear, and convey value to the patient for chosing us over anyone else ( we offer primary care, preventive medicine, urgen care and functional medicine with 24 hour direct access to care with some of our strengths including focus on individualized care, cutting edge medicine, blended functional and traditional style. We aim to transform lives through patient centered innovative and individualized care plan. I have attached a "mock" image but the details ( office address, name, phone number are incorrect) The correct info is Harborline Family Clinic 4187 Wrenfield Ave Suite 214, Clearwater, FL 33759 and phone number (727)482-3095. A possible hook could read: welcoming new patients now- Your Health, Your Time, Your Way: Personalized Care Meets Modern Medicine
Updates

I did not realize that there was a tab with more information to fill for the designers to see, or for me to upload the basic information they need to create the design.

Target Market(s)

Patients over 18 years of age with interest in longevity, functional and traditional medicine; the postcards will be mailed to our CURRENT patients, and they are a reminder of what we do, new patient availability AND a request for them to refer friends or families

Industry/Entity Type

medical

Font styles to use
Sans Serif

Colors

Designer to choose colors to be used in the design.

Requirements
Must have
• simple reminder to current patients of what we offer, and a call to action for our patients to refer friends and family for same level of excellence;consistency with brand ( see business card and cmyx codes for colors);photo of new physician; logo Harborline Family Clinic, web site (https://harborlinefamilyclinic.net); Must clearly express accepting new patients; simple to call/email to schedule free consultation;; include our email (office@harborlinefamilyclinic.org), phone number (727)482-3095; our address 4187 Wrenfield Ave Suite 214, Clearwater, FL 33759
Nice to have
• photo of our new physician ( in blue jacket: Dr. Malvina Okoruwe, MD) should not take up too much space
Should not have
• clutter, or close text; full sentences( bulleted text preferred)

```html
<!DOCTYPE html>
<html lang="en">
<head>
<meta charset="utf-8">
<title>Harborline Family Clinic – Postcard</title>
<link rel="stylesheet" href="https://fonts.googleapis.com/css2?family=Archivo:ital,wght@0,300;0,400;0,500;0,700;0,800;1,500&family=Montserrat:wght@500;600&family=Roboto:wght@300;400&display=swap">
<style>
:root{
  --board-top:#a7a8ad;
  --board-bottom:#8b8c91;
  --label:#e9e9ec;
  --brand-blue:#5e7088;
  --headline:#596a84;
  --cream:#f3f3ef;
  --tan:#cdccbe;
  --ink:#0b0b0c;
  --slate:#343b44;
  --slate-text:#3c4757;
  --muted:#e8e8e4;
  --white:#ffffff;
  --rule:#c9c9c4;
}
*{margin:0;padding:0;box-sizing:border-box}
html,body{width:898px;height:1200px;overflow:hidden}
body{background:linear-gradient(180deg,var(--board-top),var(--board-bottom));font-family:"Archivo",Arial,sans-serif;color:var(--ink);position:relative}
.abs{position:absolute}
.board-header{left:0;top:73px;width:898px;height:99px;background:linear-gradient(90deg,#8c8e93,#7a7c81);font-family:"Montserrat",sans-serif;color:var(--label)}
.board-title{left:50px;top:21px;font-size:19.5px;font-weight:600;letter-spacing:.2px}
.board-sub{left:50px;top:44px;font-size:15px;font-weight:500;line-height:18px}
.board-status{right:54px;top:57px;font-size:19.5px;font-weight:600;color:#b4b6bb}
.side-label{right:54px;font-family:"Montserrat",sans-serif;font-size:15px;font-weight:600;color:var(--label)}

/* FRONT */
.front{left:53px;top:253px;width:792px;height:432px;overflow:hidden;box-shadow:0 2px 6px rgba(0,0,0,.15)}
.front-topband{left:0;top:0;width:792px;height:38px;background:var(--brand-blue)}
.front-main{left:0;top:38px;width:515px;height:266px;background:var(--cream)}
.headline{left:25px;top:13px;font-family:"Roboto",sans-serif;font-weight:300;font-size:46px;line-height:41px;color:var(--headline);letter-spacing:-.6px}
.brand-mark{left:367px;top:40px;display:flex;align-items:flex-start;gap:8px}
.brand-dot{width:14px;height:14px;border-radius:50%;background:var(--ink);margin-top:4px}
.brand-name{font-family:"Archivo",sans-serif;font-weight:400;font-size:17px;line-height:21px;color:var(--ink)}
.tagline{left:25px;top:157px;font-size:15.5px;line-height:17px;font-weight:400}
.tagline em{font-style:italic;font-weight:500}
.front-rule{left:25px;top:202px;width:467px;height:1px;background:var(--rule)}
.services{left:0;top:214px;width:515px;height:46px}
.service{position:absolute;top:0;font-weight:800;font-size:19.5px;line-height:18px}
.vdiv{position:absolute;width:1px;background:#bdbdb7}
.share-band{left:0;top:304px;width:515px;height:57px;background:var(--tan)}
.share-title{left:23px;top:9px;font-weight:800;font-size:22px;line-height:20px;color:var(--slate-text)}
.share-copy{left:153px;top:11px;font-weight:700;font-size:16px;line-height:17px;color:var(--slate-text)}
.photo{left:515px;top:38px;width:277px;height:323px;background:linear-gradient(90deg,#e3e1da 0%,#e3e1da 30%,#d2d0c3 30%,#d2d0c3 60%,#c7c5b7 60%)}
.photo-figure{position:absolute;left:12px;bottom:0;width:255px;height:300px;border-radius:120px 120px 0 0;background:linear-gradient(180deg,rgba(40,35,40,0) 0%,rgba(40,35,45,.25) 35%,#1d1f2d 62%,#171926 100%)}
.cta-bar{left:0;top:361px;width:515px;height:71px;background:var(--ink);color:var(--white);font-weight:700;font-size:12.2px;line-height:15px}
.cta-call{left:25px;top:20px}
.cta-email{left:289px;top:20px}
.cta-bar .vdiv{left:265px;top:21px;height:30px;background:#555}
.doctor-bar{left:515px;top:361px;width:277px;height:71px;background:var(--slate);color:var(--white);text-align:center}
.doctor-name{left:0;width:277px;top:7px;font-family:"Roboto",sans-serif;font-weight:300;font-size:14px;color:#d8dbe0}
.accepting{left:0;width:277px;top:29px;font-family:"Roboto",sans-serif;font-weight:400;font-size:16px}

/* BACK */
.back{left:50px;top:721px;width:792px;height:431px;overflow:hidden;background:var(--white);box-shadow:0 2px 6px rgba(0,0,0,.15)}
.back-side{left:0;top:0;width:109px;height:358px;background:var(--ink);color:var(--white)}
.side-brand{left:19px;top:22px;display:flex;gap:5px;align-items:flex-start}
.side-brand .brand-dot{width:9px;height:9px;background:var(--white);margin-top:2px}
.side-brand .brand-name{color:var(--white);font-size:10.5px;line-height:13px}
.side-rule{position:absolute;left:19px;width:73px;height:1px;background:#777}
.side-address{left:19px;top:108px;font-family:"Roboto",sans-serif;font-weight:300;font-size:8px;line-height:9.5px}
.side-refer{left:19px;top:164px;width:88px;font-family:"Roboto",sans-serif;font-weight:300;font-size:11.6px;line-height:13px}
.side-offer{left:19px;top:301px;font-weight:700;font-size:11.5px;line-height:12.5px}
.back-topband{left:109px;top:0;width:352px;height:37px;background:var(--brand-blue)}
.back-intro{left:109px;top:37px;width:352px;height:103px;background:var(--cream)}
.back-heading{left:18px;top:10px;font-weight:500;font-size:15.4px;line-height:15.5px;letter-spacing:-.2px}
.back-rule{left:18px;top:55px;width:313px;height:1px;background:var(--rule)}
.back-lead{left:18px;top:64px;font-family:"Roboto",sans-serif;font-weight:300;font-size:12px;line-height:14.5px;color:#333}
.benefits{left:109px;top:140px;width:352px;height:98px;background:var(--tan)}
.bullets{list-style:none;position:absolute}
.bullets li{position:relative;padding-left:17px}
.bullets li::before{content:"";position:absolute;left:2px;width:3px;height:3px;border-radius:50%;background:var(--ink)}
.benefits .bullets{left:18px;top:14px;width:330px;font-family:"Roboto",sans-serif;font-weight:300;font-size:9.8px;line-height:18px;letter-spacing:-.25px;color:#222;white-space:nowrap}
.benefits .bullets li::before{top:8px}
.features{left:109px;top:238px;width:217px;height:120px;background:var(--cream)}
.features .bullets{left:18px;top:11px;width:195px;font-weight:500;font-size:9px;line-height:10px}
.features .bullets li{margin-bottom:6px}
.features .bullets li::before{top:4px}
.meet{left:326px;top:238px;width:135px;height:120px;background:var(--muted);font-size:8.6px;line-height:10px;color:#222}
.meet-text{left:11px;top:13px;width:98px}
.meet-text b{font-weight:700;display:block;font-size:9px;white-space:nowrap}
.back-footer{left:0;top:358px;width:461px;height:73px;background:var(--slate);color:var(--white);font-size:9px;line-height:11px}
.footer-address{left:19px;top:25px;font-weight:700}
.footer-contact{left:151px;top:25px;font-weight:400}
.back-footer .vdiv{left:130px;top:20px;height:33px;background:#8a9099}
.stamp-box{left:702px;top:0;width:90px;height:90px;border-left:1px solid #ddd;border-bottom:1px solid #ddd}
.address-box{left:504px;top:216px;width:288px;height:215px;border-left:1px solid #ddd;border-top:1px solid #ddd}
</style>
</head>
<body>

<header class="abs board-header">
  <div class="abs board-title">HARBORLINE FAMILY CLINIC</div>
  <div class="abs board-sub">POSTCARD DESIGN<br>SIZE: 11X6</div>
  <div class="abs board-status">FINAL VERSION</div>
</header>

<div class="abs side-label" style="top:227px">FRONT</div>

<section class="abs front" aria-label="Postcard front">
  <div class="abs front-topband"></div>
  <div class="abs front-main">
    <h1 class="abs headline">Your Health,<br>Your Time,<br>Your Way</h1>
    <div class="abs brand-mark">
      <span class="brand-dot"></span>
      <span class="brand-name">Harborline<br>Family<br>Clinic</span>
    </div>
    <p class="abs tagline">Personalized Care<br><em>Meets Modern Medicine</em></p>
    <div class="abs front-rule"></div>
    <div class="abs services">
      <span class="service" style="left:23px">Primary<br>Care</span>
      <span class="vdiv" style="left:118px;top:-5px;height:44px"></span>
      <span class="service" style="left:141px">Preventive<br>Medicine</span>
      <span class="vdiv" style="left:263px;top:-5px;height:44px"></span>
      <span class="service" style="left:285px">Urgent<br>Care</span>
      <span class="vdiv" style="left:371px;top:-5px;height:44px"></span>
      <span class="service" style="left:393px">Functional<br>Medicine</span>
    </div>
  </div>
  <div class="abs share-band">
    <div class="abs share-title">Share the<br>Care!</div>
    <span class="vdiv" style="left:137px;top:10px;height:38px;background:#f2f2ec"></span>
    <div class="abs share-copy">Refer Your Friends and Family to Experience<br>Exceptional Concierge Medicine!</div>
  </div>
  <div class="abs photo" role="img" aria-label="Portrait photo of Dr. Malvina Okoruwe in a navy jacket against a light striped backdrop">
    <div class="photo-figure"></div>
  </div>
  <div class="abs cta-bar">
    <div class="abs cta-call">Schedule your free consultation today!<br>Call (727) 482-3095</div>
    <span class="vdiv"></span>
    <div class="abs cta-email">or email us at<br>office@harborlinefamilyclinic.org</div>
  </div>
  <div class="abs doctor-bar">
    <div class="abs doctor-name">Dr. Malvina Okoruwe, MD</div>
    <div class="abs accepting">Now Accepting New Patients!</div>
  </div>
</section>

<div class="abs side-label" style="top:694px">BACK</div>

<section class="abs back" aria-label="Postcard back">
  <aside class="abs back-side">
    <div class="abs side-brand">
      <span class="brand-dot"></span>
      <span class="brand-name">Harborline<br>Family<br>Clinic</span>
    </div>
    <span class="side-rule" style="top:95px"></span>
    <div class="abs side-address">4187 Wrenfield Ave,<br>Suite 214, Clearwater,<br>FL 33759</div>
    <span class="side-rule" style="top:148px"></span>
    <p class="abs side-refer">Already part of the Harborline Family Clinic family? Refer a friend or loved one and share the benefits of our concierge care!</p>
    <span class="side-rule" style="top:289px"></span>
    <div class="abs side-offer">FREE<br>Consultation<br>for New<br>Patients!</div>
  </aside>

  <div class="abs back-topband"></div>
  <div class="abs back-intro">
    <h2 class="abs back-heading">Discover Personalized, Concierge Medicine<br>Tailored Just for You!</h2>
    <div class="abs back-rule"></div>
    <p class="abs back-lead">At Harborline Family Clinic, we combine modern medicine<br>with personalized attention to help you thrive.</p>
  </div>
  <div class="abs benefits">
    <ul class="bullets">
      <li>24-hour direct access to personalized, innovative care</li>
      <li>One-hour or more visits, flexible appointments via Vidlyn, phone, or in-office</li>
      <li>Cutting-edge medicine blending functional and traditional approaches</li>
      <li>No insurance hassles – we focus on YOU and your health goals</li>
    </ul>
  </div>
  <div class="abs features">
    <ul class="bullets">
      <li>Long-term, personal relationship with your personal physician</li>
      <li>Industry-leading low doctor/patient ratio</li>
      <li>Best-in-class acute and preventive care services</li>
      <li>Complete care coordination</li>
      <li>Travel medicine, and more...</li>
    </ul>
  </div>
  <div class="abs meet">
    <p class="abs meet-text"><b>Meet<br>Dr. Malvina Okoruwe, MD,</b><span style="display:block;height:3px"></span>and explore how we can help you achieve your health goals. Call today to book your complimentary 30-minute consultation!</p>
  </div>
  <footer class="abs back-footer">
    <div class="abs footer-address">4187 Wrenfield Ave,<br>Suite 214, Clearwater,<br>FL 33759</div>
    <span class="vdiv"></span>
    <div class="abs footer-contact">Phone: (727) 482-3095<br>Email: office@harborlinefamilyclinic.org<br>Website: www.harborlinefamilyclinic.net</div>
  </footer>
  <div class="abs stamp-box"></div>
  <div class="abs address-box"></div>
</section>

</body>
</html>
```